GDFH Business Card

Looking for a business card design to incorporate our branding. We want to only use the colors listing in the Branding Package (attached).
Updates

Target Market(s)

People who need their phone or device fixed.

Industry/Entity Type

Electronics

Contact Information for Business Card

Please use:

Gadget Fix Haven LLC
4870 S Ridgecrest Pkwy
Suite 318
San Antonio, TX 78291

Wendell Thorsby, Store Manager

(210) 555-0147

Requirements
Must have
• Must include the colors that are contained within the Branding Package PDF file.

```html
<!DOCTYPE html>
<html lang="en">
<head>
<meta charset="utf-8">
<title>GDFH Business Card</title>
<link rel="stylesheet" href="https://fonts.googleapis.com/css2?family=Montserrat:wght@400;500;600&display=swap">
<style>
  :root {
    --backdrop: #c4e8dc;
    --card-top: #a3c3c7;
    --card-bottom: #8fb2b7;
    --orange: #f0561f;
    --amber: #fbb73a;
    --lime: #d3de58;
    --ink: #4a5558;
  }
  * { margin: 0; padding: 0; box-sizing: border-box; }
  html, body { width: 1200px; height: 960px; overflow: hidden; }
  body {
    background: var(--backdrop);
    font-family: "Montserrat", sans-serif;
    position: relative;
  }
  .card {
    position: absolute;
    width: 560px;
    height: 320px;
    border-radius: 36px;
    overflow: hidden;
    background: linear-gradient(180deg, var(--card-top), var(--card-bottom));
    box-shadow: 0 14px 30px rgba(40, 90, 80, 0.22);
  }
  .card-front { left: 560px; top: 90px; }
  .card-back { left: 80px; top: 520px; }
  .card-art { position: absolute; inset: 0; width: 100%; height: 100%; }

  .brand {
    position: absolute;
    left: 120px;
    top: 126px;
    display: flex;
    align-items: center;
    gap: 14px;
  }
  .brand-mark {
    width: 50px; height: 50px;
    background: var(--orange);
    border-radius: 8px;
  }
  .brand-name {
    color: var(--orange);
    font-weight: 500;
    font-size: 30px;
    letter-spacing: 0.5px;
  }

  .contact {
    position: absolute;
    left: 238px;
    top: 74px;
    right: 30px;
    color: var(--ink);
  }
  .contact-name {
    color: var(--orange);
    font-weight: 600;
    font-size: 22px;
    letter-spacing: 1px;
    text-transform: uppercase;
  }
  .contact-role { font-size: 14px; margin-top: 2px; }
  .contact-list { list-style: none; margin-top: 34px; }
  .contact-item {
    display: flex;
    align-items: center;
    gap: 14px;
    font-size: 15px;
    line-height: 1.3;
    margin-bottom: 12px;
  }
  .contact-icon {
    flex: none;
    width: 32px; height: 32px;
    border-radius: 50%;
    background: var(--orange);
    display: flex; align-items: center; justify-content: center;
  }
  .contact-icon svg { width: 18px; height: 18px; }
</style>
</head>
<body>

<section class="card card-front" aria-label="Card front">
  <svg class="card-art" viewBox="0 0 560 320" preserveAspectRatio="none" aria-hidden="true">
    <polygon points="0,200 110,250 150,320 0,320" fill="var(--lime)"/>
    <polygon points="440,0 560,0 560,230 490,230" fill="var(--orange)"/>
    <polygon points="440,0 466,0 486,130 462,130" fill="var(--amber)"/>
    <line x1="466" y1="0" x2="492" y2="230" stroke="var(--lime)" stroke-width="2"/>
  </svg>
  <div class="brand">
    <span class="brand-mark"></span>
    <span class="brand-name">Gadget Fix Haven</span>
  </div>
</section>

<section class="card card-back" aria-label="Card back">
  <svg class="card-art" viewBox="0 0 560 320" preserveAspectRatio="none" aria-hidden="true">
    <polygon points="0,0 170,0 150,320 0,320" fill="var(--orange)"/>
    <polygon points="168,140 205,150 195,320 158,320" fill="var(--amber)"/>
    <line x1="172" y1="0" x2="152" y2="320" stroke="var(--lime)" stroke-width="2"/>
    <polygon points="380,0 470,0 560,110 560,130 390,40" fill="var(--lime)"/>
  </svg>
  <div class="contact">
    <h1 class="contact-name">Wendell Thorsby</h1>
    <p class="contact-role">Store Manager</p>
    <ul class="contact-list">
      <li class="contact-item">
        <span class="contact-icon">
          <svg viewBox="0 0 24 24"><path d="M12 2a7 7 0 0 0-7 7c0 5 7 13 7 13s7-8 7-13a7 7 0 0 0-7-7zm0 9.5A2.5 2.5 0 1 1 12 6.5a2.5 2.5 0 0 1 0 5z" fill="var(--amber)"/></svg>
        </span>
        <span>4870 S Ridgecrest Pkwy<br>Suite 318, San Antonio, TX 78291</span>
      </li>
      <li class="contact-item">
        <span class="contact-icon">
          <svg viewBox="0 0 24 24"><path d="M6.6 10.8a15 15 0 0 0 6.6 6.6l2.2-2.2a1 1 0 0 1 1-.25 11.4 11.4 0 0 0 3.6.57 1 1 0 0 1 1 1V20a1 1 0 0 1-1 1A17 17 0 0 1 3 4a1 1 0 0 1 1-1h3.5a1 1 0 0 1 1 1c0 1.25.2 2.45.57 3.57a1 1 0 0 1-.25 1z" fill="var(--amber)"/></svg>
        </span>
        <span>(210) 555-0147</span>
      </li>
      <li class="contact-item">
        <span class="contact-icon">
          <svg viewBox="0 0 24 24"><path d="M3 6h18v12H3z" fill="none" stroke="var(--amber)" stroke-width="2"/><path d="M3 6l9 7 9-7" fill="none" stroke="var(--amber)" stroke-width="2"/></svg>
        </span>
        <span>wthorsby@gdfhmail.com</span>
      </li>
    </ul>
  </div>
</section>

</body>
</html>
```